Business card por a urban DJ, up scale audience target

Need a sober design, modern, conservative colors but i can consider some options, y play rnb, hip hop, EDM and top40.

Business card for contact and personal info, double sided, use logo attrached please; im 42 so i need a card acording to my age an target audience.

Target Market(s)

Adult people, up scale audience

Industry/Entity Type

Music Download

Contact Information for Business Card

Cel (318) 5024471963 www.kelvarodun.com

Requirements
Must have
• open mind
Nice to have
• open mind
Should not have
• DJ

```html
<!DOCTYPE html>
<html lang="en">
<head>
<meta charset="utf-8">
<title>Kelva — Business Card</title>
<link href="https://fonts.googleapis.com/css2?family=Open+Sans:wght@400;700;800&display=swap" rel="stylesheet">
<style>
  :root {
    --page: #2b2b2b;
    --card: #050505;
    --ink: #c9c9c9;
    --ink-soft: #a8a8a8;
  }
  html, body {
    margin: 0;
    width: 1200px;
    height: 900px;
    overflow: hidden;
    background: var(--page);
    font-family: "Open Sans", sans-serif;
  }
  .sheet {
    position: relative;
    width: 1200px;
    height: 900px;
  }
  .card {
    position: absolute;
    left: 250px;
    width: 700px;
    height: 400px;
    background: var(--card);
    overflow: hidden;
    box-shadow: 0 10px 30px rgba(0,0,0,0.45);
  }
  .card--front { top: 30px; }
  .card--back { top: 470px; }

  .front-mark {
    position: absolute;
    left: 0; right: 0;
    top: 100px;
    text-align: center;
    color: var(--ink);
    font-weight: 800;
    font-size: 120px;
    line-height: 1;
    letter-spacing: 2px;
  }
  .front-url {
    position: absolute;
    left: 0; right: 0;
    top: 255px;
    text-align: center;
    color: var(--ink);
    font-weight: 400;
    font-size: 24px;
    letter-spacing: 6px;
  }

  .eq-bars { position: absolute; left: 0; top: 0; }
  .eq-bars rect { fill: var(--ink); }

  .back-mark {
    position: absolute;
    left: 185px;
    top: 62px;
    color: var(--ink);
    font-weight: 800;
    font-size: 64px;
    line-height: 1;
    letter-spacing: 1px;
  }
  .holder {
    position: absolute;
    left: 200px;
    top: 352px;
    text-align: right;
    color: var(--ink);
  }
  .holder-name { font-weight: 700; font-size: 19px; line-height: 1.1; }
  .holder-role { font-size: 10px; letter-spacing: 1px; color: var(--ink-soft); }
  .divider {
    position: absolute;
    left: 378px;
    top: 340px;
    width: 1px;
    height: 44px;
    background: var(--ink-soft);
  }
  .contacts {
    position: absolute;
    left: 390px;
    top: 340px;
    color: var(--ink);
    font-size: 13px;
    line-height: 20px;
  }
  .contact-line { display: flex; align-items: center; gap: 6px; }
  .contact-line svg { flex: none; }
</style>
</head>
<body>
<main class="sheet">
  <section class="card card--front">
    <div class="front-mark">KELVA</div>
    <div class="front-url">www.kelvarodun.com</div>
  </section>

  <section class="card card--back">
    <svg class="eq-bars" width="700" height="400" viewBox="0 0 700 400" aria-hidden="true">
      <rect x="2" y="315" width="12" height="30"/><rect x="18" y="325" width="12" height="20"/>
      <rect x="34" y="309" width="12" height="36"/><rect x="50" y="331" width="12" height="14"/>
      <rect x="66" y="291" width="12" height="26"/><rect x="82" y="307" width="12" height="10"/>
      <rect x="98" y="285" width="12" height="32"/><rect x="114" y="299" width="12" height="18"/>
      <rect x="130" y="265" width="12" height="24"/><rect x="146" y="281" width="12" height="8"/>
      <rect x="162" y="255" width="12" height="34"/><rect x="178" y="267" width="12" height="22"/>
      <rect x="194" y="231" width="12" height="30"/><rect x="210" y="241" width="12" height="20"/>
      <rect x="226" y="225" width="12" height="36"/><rect x="242" y="247" width="12" height="14"/>
      <rect x="258" y="207" width="12" height="26"/><rect x="274" y="223" width="12" height="10"/>
      <rect x="290" y="201" width="12" height="32"/><rect x="306" y="215" width="12" height="18"/>
      <rect x="322" y="181" width="12" height="24"/><rect x="338" y="197" width="12" height="8"/>
      <rect x="354" y="171" width="12" height="34"/><rect x="370" y="183" width="12" height="22"/>
      <rect x="386" y="147" width="12" height="30"/><rect x="402" y="157" width="12" height="20"/>
      <rect x="418" y="141" width="12" height="36"/><rect x="434" y="163" width="12" height="14"/>
      <rect x="450" y="123" width="12" height="26"/><rect x="466" y="139" width="12" height="10"/>
      <rect x="482" y="117" width="12" height="32"/><rect x="498" y="131" width="12" height="18"/>
      <rect x="514" y="97" width="12" height="24"/><rect x="530" y="113" width="12" height="8"/>
      <rect x="546" y="87" width="12" height="34"/><rect x="562" y="99" width="12" height="22"/>
      <rect x="578" y="63" width="12" height="30"/><rect x="594" y="73" width="12" height="20"/>
      <rect x="610" y="57" width="12" height="36"/><rect x="626" y="79" width="12" height="14"/>
      <rect x="642" y="39" width="12" height="26"/><rect x="658" y="55" width="12" height="10"/>
      <rect x="674" y="33" width="12" height="32"/><rect x="690" y="47" width="12" height="18"/>
    </svg>

    <div class="back-mark">KELVA</div>

    <div class="holder">
      <div class="holder-name">Rafael Onder</div>
      <div class="holder-role">CEO</div>
    </div>
    <div class="divider"></div>
    <div class="contacts">
      <div class="contact-line">
        <svg width="9" height="13" viewBox="0 0 9 13" aria-hidden="true">
          <rect x="0.75" y="0.75" width="7.5" height="11.5" rx="1.5" fill="none" stroke="#c9c9c9" stroke-width="1.3"/>
          <circle cx="4.5" cy="10" r="0.9" fill="#c9c9c9"/>
        </svg>
        <span>(318) 5024471963</span>
      </div>
      <div class="contact-line">
        <svg width="11" height="11" viewBox="0 0 11 11" aria-hidden="true">
          <circle cx="5.5" cy="5.5" r="4.8" fill="none" stroke="#c9c9c9" stroke-width="1.1"/>
          <ellipse cx="5.5" cy="5.5" rx="2" ry="4.8" fill="none" stroke="#c9c9c9" stroke-width="0.9"/>
          <line x1="0.7" y1="5.5" x2="10.3" y2="5.5" stroke="#c9c9c9" stroke-width="0.9"/>
        </svg>
        <span>www.kelvarodun.com</span>
      </div>
    </div>
  </section>
</main>
</body>
</html>
```